Coffee Label Design - for university branded coffee

You will be design a new coffee pacakge, specifically a full color label for 12oz and 16oz bags.
Important: For all designs we purchase, the designers must complete the attached Copyright Transfer Agreement.pdf file and return to copyright@brewvanetrading.com.
Please use the CoffeeLabelTemplate.ai file for proper sizing, color mode (CYMK) and resolution. The area in the golden box near the bottom MUST be left empty. All other areas can be used for your design.
A specification document is attach.
Please note we often chose 2nd and 3rd place designs, and compensate for all selected designs.
Target Market(s)
See the attached design brief
Requirements
Must have
- See the attached design brief
Nice to have

```html
<!DOCTYPE html>
<html lang="en">
<head>
<meta charset="utf-8">
<title>1905 Breakfast Blend Coffee Label</title>
<link href="https://fonts.googleapis.com/css2?family=Abril+Fatface&family=Oswald:wght@500;600&family=Montserrat:wght@600;700;800&display=swap" rel="stylesheet">
<style>
  :root {
    --maroon: #6a1e25;
    --maroon-deep: #5a161d;
    --maroon-soft: #7a2c32;
    --cream: #f4ecdc;
    --orange: #f0882c;
    --white: #ffffff;
  }
  * { margin: 0; padding: 0; box-sizing: border-box; }
  html, body { width: 800px; height: 1200px; overflow: hidden; background: var(--cream); }
  .label {
    position: relative;
    width: 800px;
    height: 1200px;
    overflow: hidden;
    background: var(--maroon);
    font-family: "Montserrat", sans-serif;
  }
  .petal-pattern {
    position: absolute;
    left: 0; top: 0;
    width: 800px; height: 693px;
    background: radial-gradient(ellipse at 50% 45%, var(--maroon-soft) 0%, var(--maroon) 55%, var(--maroon-deep) 100%);
  }
  .brand-tab {
    position: absolute;
    left: 331px; top: 0;
    width: 136px; height: 139px;
    background: var(--cream);
    display: flex; flex-direction: column;
    align-items: center; justify-content: center;
    gap: 10px;
  }
  .brand-tab::after {
    content: "";
    position: absolute;
    left: 8px; right: 8px; top: 0; bottom: 8px;
    border: 3px solid var(--maroon);
    border-top: none;
  }
  .brand-mark {
    width: 34px; height: 34px;
    border-radius: 50%;
    background: var(--maroon);
  }
  .brand-name {
    font-family: "Oswald", sans-serif;
    font-weight: 600;
    font-size: 22px;
    letter-spacing: 2px;
    color: var(--maroon);
    text-transform: uppercase;
  }
  .tagline {
    position: absolute;
    top: 322px; left: 0; width: 800px;
    text-align: center;
    color: var(--cream);
    font-weight: 800;
    font-size: 22px;
    letter-spacing: 1px;
  }
  .year {
    position: absolute;
    top: 350px; left: 0; width: 800px;
    text-align: center;
    color: var(--cream);
    font-family: "Abril Fatface", serif;
    font-size: 190px;
    line-height: 1;
    letter-spacing: -2px;
  }
  .year-rule {
    position: absolute;
    top: 566px; left: 214px;
    width: 386px; height: 4px;
    background: var(--cream);
  }
  .divider-line {
    position: absolute;
    top: 693px; left: 0;
    width: 800px; height: 8px;
    background: var(--cream);
  }
  .name-band {
    position: absolute;
    top: 752px; left: 0;
    width: 800px; height: 96px;
    background: var(--cream);
    display: flex; align-items: center; justify-content: center;
  }
  .product-name {
    font-family: "Oswald", sans-serif;
    font-weight: 500;
    font-size: 54px;
    letter-spacing: 2px;
    color: var(--maroon);
  }
  .roast-panel {
    position: absolute;
    top: 875px; left: 0;
    width: 800px; height: 325px;
    background: var(--orange);
  }
  .roast-level {
    position: absolute;
    top: 960px; left: 75px;
    color: var(--maroon);
    font-weight: 800;
    font-size: 31px;
  }
  .bean-origin {
    position: absolute;
    top: 1003px; left: 75px;
    color: var(--white);
    font-weight: 700;
    font-size: 17px;
    letter-spacing: 0.5px;
  }
  .net-volume {
    position: absolute;
    top: 1088px; left: 75px;
    color: var(--white);
    font-weight: 600;
    font-size: 24px;
  }
  .cup-illustration {
    position: absolute;
    left: 427px; top: 866px;
    width: 350px; height: 260px;
    border-radius: 40% 40% 50% 50%;
    background: radial-gradient(ellipse at 50% 40%, var(--white) 0%, #f1e6dc 45%, #e5c9b6 75%, rgba(240,136,44,0) 100%);
  }
</style>
</head>
<body>
  <main class="label">
    <div class="petal-pattern" role="img" aria-label="Outlined flower petal pattern in soft maroon"></div>

    <div class="brand-tab">
      <span class="brand-mark"></span>
      <span class="brand-name">Halden</span>
    </div>

    <p class="tagline">PREMIUM TASTE</p>
    <h1 class="year">1905</h1>
    <div class="year-rule"></div>

    <div class="divider-line"></div>

    <div class="roast-panel"></div>

    <div class="name-band">
      <h2 class="product-name">BREAKFAST BLEND</h2>
    </div>

    <p class="roast-level">MEDIUM ROAST</p>
    <p class="bean-origin">100% ARABICA CAFFEE</p>
    <p class="net-volume">16 FL.oz</p>

    <div class="cup-illustration" role="img" aria-label="Illustration of a white coffee cup on a saucer with a spoon and coffee beans"></div>
  </main>
</body>
</html>
```